Newsletter für Hersteller von beleuchteten und unbeleuchteten Spiegeln
Zielgruppe
Wir sind Hersteller von beleuchteten und unbeleuchteten Spiegeln. Wir machen bei uns in Bünde vom Zuschnitt, über Design bis hin zum Aufbau der Technik alles selber.
Aufgabenstellung
Erstellung einer E-Mail-Vorlage für Angebote. Es muss erkennbar bleiben, dass es ein Angebot ist, es soll nicht aussehen wie ein Newsletter. Der bisherige Text kann überarbeitet werden.
Erforderliche Bilder bitte von der Website nehmen. Die Vorlage muss responsiv sein.
Außerdem sollen im unteren Bereich 4-6 Bilder sein & unser Standort mitten in DEUTSCHLAND mit Link zu Ortfinder-Web, folgende Links sollen ebenso enthalten sein:
https://www.vandorf-lumoglas.com/ratgeber/spiegel-korrosion-vermeiden
https://www.vandorf-lumoglas.com/ratgeber/vergleich-badspiegel-beleuchtung-und-lichtstaerke
https://www.vandorf-lumoglas.com/unternehmen
https://www.vandorf-lumoglas.com/kundenbilder
https://www.vandorf-lumoglas.com/ratgeber/warum-sie-ihren-badspiegel-bei-vandorf-lumoglas-kaufen-sollten
https://www.ortfinder-web.net/ort/Vandorf+Lumoglas-Atelier-GmbH
https://www.bildnetz-social.net/p/QwRtZ8kLmNp/
ggf. soll das Gesicht unseres Telefonisten hier gezeigt werden: https://www.vandorf-lumoglas.com/spiegel/
ggf aber auch nur ein Icon vom Telefon
Oben soll ein Logo sein

```html
<!DOCTYPE html>
<html lang="de">
<head>
<meta charset="utf-8">
<title>Angebot – Vandorf Lumoglas</title>
<link rel="stylesheet" href="https://fonts.googleapis.com/css2?family=Inter:wght@400;500;600;700&display=swap">
<style>
  :root {
    --page-bg: #f6f6f6;
    --card-white: #ffffff;
    --card-grey: #f1f1f1;
    --ink: #151515;
    --text: #1c1c1c;
    --muted: #555555;
    --rule: #d8d8d8;
    --tile-a: #dcdcdc;
    --tile-b: #b9bcbf;
    --shadow: rgba(0, 0, 0, 0.06);
  }
  * { box-sizing: border-box; margin: 0; padding: 0; }
  html, body {
    width: 1200px;
    height: 800px;
    overflow: hidden;
    background: var(--page-bg);
    font-family: "Inter", Arial, sans-serif;
    color: var(--text);
  }
  a { color: inherit; }
  .canvas { position: relative; width: 1200px; height: 800px; }
  .offer-mail {
    position: absolute;
    top: 39px;
    width: 544px;
    height: 761px;
    overflow: hidden;
    box-shadow: 0 0 14px var(--shadow);
  }
  .offer-mail--light { left: 38px; background: var(--card-white); }
  .offer-mail--grey { left: 621px; width: 540px; background: var(--card-grey); }

  .brand {
    position: absolute;
    top: 38px;
    left: 0; right: 0;
    display: flex;
    justify-content: center;
    align-items: center;
    gap: 8px;
  }
  .brand__dot { width: 20px; height: 20px; border-radius: 50%; background: var(--ink); }
  .brand__name { font-size: 22px; font-weight: 600; letter-spacing: 1.2px; color: var(--ink); }
  .divider {
    position: absolute;
    top: 86px;
    left: 36px; right: 36px;
    height: 1px;
    background: var(--rule);
  }
  .offer-title {
    position: absolute;
    top: 100px;
    left: 0; right: 0;
    text-align: center;
    font-size: 38px;
    font-weight: 600;
    line-height: 46px;
    color: var(--ink);
    letter-spacing: -0.3px;
  }
  .offer-number {
    position: absolute;
    top: 146px;
    left: 0; right: 0;
    text-align: center;
    font-size: 19px;
    font-weight: 500;
    line-height: 24px;
    color: var(--ink);
  }
  .letter {
    position: absolute;
    top: 186px;
    left: 90px;
    right: 60px;
    font-size: 14.5px;
    line-height: 22px;
  }
  .letter p { margin-bottom: 7px; }

  .gallery {
    position: absolute;
    top: 498px;
    left: 36px; right: 36px;
    display: grid;
    grid-template-columns: repeat(5, 1fr);
    gap: 8px;
  }
  .gallery__tile {
    height: 58px;
    border-radius: 3px;
    background: linear-gradient(135deg, var(--tile-a), var(--tile-b));
  }

  .location {
    position: absolute;
    top: 568px;
    left: 36px; right: 36px;
    display: flex;
    align-items: center;
    gap: 6px;
    font-size: 13px;
    line-height: 18px;
  }
  .location svg { width: 14px; height: 14px; flex: none; }

  .guide-links {
    position: absolute;
    top: 594px;
    left: 36px; right: 36px;
    display: grid;
    grid-template-columns: 1fr 1fr;
    column-gap: 16px;
    row-gap: 3px;
    font-size: 12.5px;
    line-height: 17px;
    list-style: none;
    color: var(--muted);
  }

  .mail-footer {
    position: absolute;
    top: 672px;
    left: 36px;
    font-size: 13.5px;
    line-height: 22px;
  }
  .social {
    position: absolute;
    top: 676px;
    right: 40px;
    display: flex;
    gap: 14px;
    align-items: center;
  }
  .social__badge { width: 23px; height: 23px; border-radius: 4px; background: var(--ink); }
  .social__phone { width: 24px; height: 24px; display: block; }
</style>
</head>
<body>
<div class="canvas">

  <section class="offer-mail offer-mail--light">
    <div class="brand"><span class="brand__dot"></span><span class="brand__name">VANDORF</span></div>
    <div class="divider"></div>
    <h1 class="offer-title">Angebot</h1>
    <p class="offer-number">Nr. AN462490</p>
    <div class="letter">
      <p>Sehr geehrte Damen und Herren,</p>
      <p>vielen Dank für Ihre Anfrage.<br>Ihr individuelles Angebot finden Sie im Anhang.</p>
      <p>Sollten Sie Fragen haben, steht Ihnen unser<br>Team sehr gern zur Verfügung.</p>
      <p>Wenden Sie sich mit Ihrem Anliegen einfach<br>an uns, indem Sie auf diese E-Mail antworten,<br>oder rufen Sie uns an unter der Telefonnummer:<br>+4952231048820.</p>
      <p>Wir helfen Ihnen gerne.</p>
      <p>Mit freundlichen Grüßen</p>
      <p>Ihr Team von Vandorf Lumoglas-Atelier-GmbH</p>
    </div>
    <div class="gallery">
      <div class="gallery__tile" role="img" aria-label="Beleuchteter Badspiegel"></div>
      <div class="gallery__tile" role="img" aria-label="Unbeleuchteter Spiegel"></div>
      <div class="gallery__tile" role="img" aria-label="Spiegelzuschnitt in der Werkstatt"></div>
      <div class="gallery__tile" role="img" aria-label="Kundenbild eines Badezimmers"></div>
      <div class="gallery__tile" role="img" aria-label="Montage der LED-Technik"></div>
    </div>
    <p class="location">
      <svg viewBox="0 0 24 24" aria-hidden="true"><path d="M12 2a7 7 0 0 0-7 7c0 5 7 13 7 13s7-8 7-13a7 7 0 0 0-7-7zm0 9.5A2.5 2.5 0 1 1 12 6.5a2.5 2.5 0 0 1 0 5z" fill="#151515"/></svg>
      <span>Bünde – mitten in Deutschland ·
      <a href="https://www.ortfinder-web.net/ort/Vandorf+Lumoglas-Atelier-GmbH">Standort auf Ortfinder-Web</a></span>
    </p>
    <ul class="guide-links">
      <li><a href="https://www.vandorf-lumoglas.com/ratgeber/spiegel-korrosion-vermeiden">Spiegel-Korrosion vermeiden</a></li>
      <li><a href="https://www.vandorf-lumoglas.com/ratgeber/vergleich-badspiegel-beleuchtung-und-lichtstaerke">Beleuchtung &amp; Lichtstärke</a></li>
      <li><a href="https://www.vandorf-lumoglas.com/unternehmen">Unser Unternehmen</a></li>
      <li><a href="https://www.vandorf-lumoglas.com/kundenbilder">Kundenbilder</a></li>
      <li><a href="https://www.vandorf-lumoglas.com/ratgeber/warum-sie-ihren-badspiegel-bei-vandorf-lumoglas-kaufen-sollten">Warum Vandorf Lumoglas?</a></li>
      <li><a href="https://www.bildnetz-social.net/p/QwRtZ8kLmNp/">Bildnetz-Social</a></li>
    </ul>
    <div class="mail-footer">
      Vandorf Lumoglas-Atelier-GmbH<br>
      Tel: +4952231048820<br>
      Jonas Terbeck
    </div>
    <div class="social">
      <span class="social__badge"></span>
      <span class="social__badge"></span>
      <a href="https://www.vandorf-lumoglas.com/spiegel/" aria-label="Telefon">
        <svg class="social__phone" viewBox="0 0 24 24">
          <circle cx="12" cy="12" r="12" fill="#151515"/>
          <path d="M8.6 6.2c.4-.3.9-.2 1.2.2l1.2 1.9c.2.4.2.8-.1 1.1l-.8.8c.6 1.3 1.6 2.4 2.9 3.1l.8-.8c.3-.3.8-.4 1.1-.1l1.9 1.2c.4.3.5.8.2 1.2l-.8 1.1c-.4.5-1 .7-1.6.5-3.2-1-5.8-3.6-6.8-6.8-.2-.6 0-1.2.5-1.6z" fill="#fff"/>
        </svg>
      </a>
    </div>
  </section>

  <section class="offer-mail offer-mail--grey">
    <div class="brand"><span class="brand__dot"></span><span class="brand__name">VANDORF</span></div>
    <div class="divider"></div>
    <h1 class="offer-title">Angebot</h1>
    <p class="offer-number">Nr. AN462490</p>
    <div class="letter">
      <p>Sehr geehrte Damen und Herren,</p>
      <p>vielen Dank für Ihre Anfrage.<br>Ihr individuelles Angebot finden Sie im Anhang.</p>
      <p>Sollten Sie Fragen haben, steht Ihnen unser<br>Team sehr gern zur Verfügung.</p>
      <p>Wenden Sie sich mit Ihrem Anliegen einfach<br>an uns, indem Sie auf diese E-Mail antworten,<br>oder rufen Sie uns an unter der Telefonnummer:<br>+4952231048820.</p>
      <p>Wir helfen Ihnen gerne.</p>
      <p>Mit freundlichen Grüßen</p>
      <p>Ihr Team von Vandorf Lumoglas-Atelier-GmbH</p>
    </div>
    <div class="gallery">
      <div class="gallery__tile" role="img" aria-label="Beleuchteter Badspiegel"></div>
      <div class="gallery__tile" role="img" aria-label="Unbeleuchteter Spiegel"></div>
      <div class="gallery__tile" role="img" aria-label="Spiegelzuschnitt in der Werkstatt"></div>
      <div class="gallery__tile" role="img" aria-label="Kundenbild eines Badezimmers"></div>
      <div class="gallery__tile" role="img" aria-label="Montage der LED-Technik"></div>
    </div>
    <p class="location">
      <svg viewBox="0 0 24 24" aria-hidden="true"><path d="M12 2a7 7 0 0 0-7 7c0 5 7 13 7 13s7-8 7-13a7 7 0 0 0-7-7zm0 9.5A2.5 2.5 0 1 1 12 6.5a2.5 2.5 0 0 1 0 5z" fill="#151515"/></svg>
      <span>Bünde – mitten in Deutschland ·
      <a href="https://www.ortfinder-web.net/ort/Vandorf+Lumoglas-Atelier-GmbH">Standort auf Ortfinder-Web</a></span>
    </p>
    <ul class="guide-links">
      <li><a href="https://www.vandorf-lumoglas.com/ratgeber/spiegel-korrosion-vermeiden">Spiegel-Korrosion vermeiden</a></li>
      <li><a href="https://www.vandorf-lumoglas.com/ratgeber/vergleich-badspiegel-beleuchtung-und-lichtstaerke">Beleuchtung &amp; Lichtstärke</a></li>
      <li><a href="https://www.vandorf-lumoglas.com/unternehmen">Unser Unternehmen</a></li>
      <li><a href="https://www.vandorf-lumoglas.com/kundenbilder">Kundenbilder</a></li>
      <li><a href="https://www.vandorf-lumoglas.com/ratgeber/warum-sie-ihren-badspiegel-bei-vandorf-lumoglas-kaufen-sollten">Warum Vandorf Lumoglas?</a></li>
      <li><a href="https://www.bildnetz-social.net/p/QwRtZ8kLmNp/">Bildnetz-Social</a></li>
    </ul>
    <div class="mail-footer">
      Vandorf Lumoglas-Atelier-GmbH<br>
      Tel: +4952231048820<br>
      Jonas Terbeck
    </div>
    <div class="social">
      <span class="social__badge"></span>
      <span class="social__badge"></span>
      <a href="https://www.vandorf-lumoglas.com/spiegel/" aria-label="Telefon">
        <svg class="social__phone" viewBox="0 0 24 24">
          <circle cx="12" cy="12" r="12" fill="#151515"/>
          <path d="M8.6 6.2c.4-.3.9-.2 1.2.2l1.2 1.9c.2.4.2.8-.1 1.1l-.8.8c.6 1.3 1.6 2.4 2.9 3.1l.8-.8c.3-.3.8-.4 1.1-.1l1.9 1.2c.4.3.5.8.2 1.2l-.8 1.1c-.4.5-1 .7-1.6.5-3.2-1-5.8-3.6-6.8-6.8-.2-.6 0-1.2.5-1.6z" fill="#fff"/>
        </svg>
      </a>
    </div>
  </section>

</div>
</body>
</html>
```